Im want a website LIKE KMT's and FleetStride.com's with product payment options like Wendaro's

I need a website LIKE KMT with a header made EXACTLY LIKE THAT OF FLEETSTRIDES .

The front page photo should be like that of FLEETSTRIDE's webpage as well.

The name of the website will be called "C.M. (Calmira Mesa)".

We will be targeting ALL MARKETS in a small town in central Panama and charging businesses "listing fees" like a phone book does but also providing informational blogs, news, and other interesting activities.

THIS IS A MULTI PAGE WEBSITE

THIS IS WHERE KMT's website meets Norvex/FleetStride.

Once the layout is built I will tweak and modify, add information, and upload items for sale.

Here is a list of specific categories that should be listed out above the front page header image/search bar

-- Home -- News -- Travel -- Activities -- Shop & Dine -- Store -- More... --

These categories should be spread across the bottom of the page in three sections:

WHATS SO GREAT ABOUT (Calmira Mesa),
HAND PICKED TOURS
ACTIVITIES etc.

Also lets use www.Wendaro.example 's
"HOT DESTINATIONS"
"BEAT THE BEST PRICES IN BOQUETE"
"OCTOBERS INSIDER PICKS"
"TOP DESTINATIONS"
and spread them in four sections side-by-side near the bottom of the page.

Overall I would like to see the finished product to be something LIKE KMT's and FleetStrides.

WE NEED ONLINE PAYMENT OPTIONS LIKE NORVEX'S WEBSITE HAS

This will be a desktop website but should be very mobile friendly as well.

-rodwell

P.S. Good luck!
Updates

If it isn't already too late to change the website name, the name of the website should be "Calmira Mesa". Added Friday, October 9, 2015

What do you guys think the budget should be to win this? Added Saturday, October 10, 2015

www.lunaverde.example is the most amazing simple site. Whoever can make me a replica with my specifications will win immediately!!!! Added Sunday, October 18, 2015

OMG www.lunaverde.example is the bomb!So simple and elegant. Whoever can make me an EXACT REPLICA OF WWW.LUNAVERDE.EXAMPLE as my site with the specifications mentioned in my brief will take home the $825.00 immediately! Good luck amigos! Added Sunday, October 18, 2015

Does anybody know how to add recurring monthly billing options on this website? Added Sunday, October 18, 2015

Target Market(s)

ALL MARKETS

Industry/Entity Type

Product

Coding

Coded - Design and coding required

Number of Pages Required

5+ page

Requirements
Must have
• Coinlark payment options.
• I must be able to add and remove photos/text and video from the HTML files in the page.
• Be creative my friends, and may the odds be forever in your favor!
Nice to have
• I added some photos of a good layout for our page below.

```html
<!DOCTYPE html>
<html lang="en">
<head>
<meta charset="utf-8">
<title>Calmira Mesa</title>
<link href="https://fonts.googleapis.com/css2?family=Roboto:wght@300;400;500;700&display=swap" rel="stylesheet">
<style>
:root{
  --blue:#1b75bb;
  --blue-dark:#0f4f86;
  --navy:#0c2c4d;
  --navy-deep:#07203a;
  --orange:#f7941d;
  --text:#555;
  --muted:#888;
  --light:#f2f4f6;
  --white:#fff;
}
*{margin:0;padding:0;box-sizing:border-box}
html,body{width:789px;height:1200px;overflow:hidden}
body{font-family:"Roboto",Arial,sans-serif;color:var(--text);background:var(--white);position:relative}

.hero-backdrop{position:absolute;left:0;top:0;width:789px;height:462px;
  background:linear-gradient(180deg,#163a5c 0%,#24639a 45%,#5b9cc9 75%,#2d5f86 100%)}

.topbar{position:absolute;top:8px;left:540px;display:flex;gap:26px;font-size:8px;color:var(--white)}
.site-header{position:absolute;top:30px;left:0;width:789px;height:48px;background:rgba(8,30,55,.55)}
.brand{position:absolute;left:105px;top:14px;display:flex;align-items:center;gap:8px}
.brand-mark{width:18px;height:18px;border-radius:50%;background:var(--orange)}
.brand-name{font-size:15px;font-weight:500;color:var(--white)}
.main-nav{position:absolute;left:284px;top:0;display:flex;height:48px}
.main-nav a{display:flex;align-items:center;padding:0 14px;font-size:9px;color:var(--white);text-decoration:none}
.main-nav a.active{background:var(--orange)}

.slider{position:absolute;left:105px;top:110px;width:584px;height:324px;border:4px solid var(--white)}
.slide-photo{position:absolute;inset:0;background:linear-gradient(180deg,#7cc4ea 0%,#b9e1f3 38%,#2fa8c8 55%,#49c0c9 68%,#e8dcb8 82%,#d9c79a 100%)}
.slide-copy{position:absolute;left:315px;top:40px;width:220px;text-align:center;color:var(--white)}
.slide-copy h1{font-size:22px;font-weight:400;margin-bottom:8px}
.slide-copy p{font-size:8px;line-height:1.5;margin-bottom:10px}
.btn{display:inline-block;background:var(--orange);color:var(--white);font-size:9px;padding:6px 16px}
.slider-arrow{position:absolute;top:146px;width:22px;height:22px;border-radius:50%;background:var(--white);display:flex;align-items:center;justify-content:center}
.slider-arrow.prev{left:-11px}.slider-arrow.next{right:-11px}

.section-title{text-align:center;font-size:20px;font-weight:400;color:var(--blue)}
.section-title span{color:var(--orange)}
.about{position:absolute;top:476px;left:0;width:789px}
.about .lead{width:470px;margin:10px auto 0;text-align:center;font-size:8px;line-height:1.6;color:var(--muted)}
.services{display:flex;justify-content:center;gap:70px;margin-top:28px}
.service{width:146px;text-align:center}
.service-icon{width:58px;height:58px;border-radius:50%;background:var(--blue-dark);margin:0 auto 14px;display:flex;align-items:center;justify-content:center}
.service h3{font-size:11px;font-weight:500;color:#333;margin-bottom:6px}
.service p{font-size:7.5px;line-height:1.55;color:var(--muted)}

.listing{position:absolute;top:740px;left:0;width:789px;height:340px;background:var(--light);padding-top:30px}
.cards{display:flex;gap:13px;justify-content:center;margin-top:22px}
.card{width:184px;background:var(--white);box-shadow:0 1px 3px rgba(0,0,0,.12)}
.card-photo{height:116px}
.card-photo.beach{background:linear-gradient(180deg,#8ccff0 0%,#bfe6f5 45%,#35b3cf 60%,#e9dcb6 100%)}
.card-photo.hammock{background:linear-gradient(160deg,#6fb8e0 0%,#d9eef7 50%,#c9b48a 100%)}
.card-photo.city{background:linear-gradient(180deg,#2e6fb2 0%,#5fa2d6 40%,#1b4e84 70%,#0d3660 100%)}
.card-body{padding:10px 10px 8px}
.card h4{font-size:9px;font-weight:400;color:var(--orange);margin-bottom:5px}
.card p{font-size:7px;line-height:1.55;color:var(--muted);margin-bottom:10px}
.card-meta{display:flex;justify-content:space-between;border-top:1px solid #eee;padding-top:7px;font-size:7px;color:var(--muted)}
.stars{color:var(--orange);letter-spacing:1px}

.contact{position:absolute;top:1086px;left:0;width:789px;height:72px;background:var(--navy)}
.contact-box{position:absolute;left:105px;top:4px;width:584px;height:62px;background:var(--blue);display:flex;align-items:center;justify-content:space-around;color:var(--white)}
.contact-item{display:flex;align-items:center;gap:8px;font-size:8px;line-height:1.4}
.contact-icon{width:22px;height:22px;border-radius:50%;background:var(--white);display:flex;align-items:center;justify-content:center}
.site-footer{position:absolute;top:1158px;left:0;width:789px;height:42px;background:var(--navy-deep);display:flex;align-items:center;padding:0 105px;font-size:6.5px;color:#9fb3c8}
.footer-links{display:flex;gap:12px}
.copyright{margin-left:26px}
.social{margin-left:auto;display:flex;gap:6px}
.social span{width:10px;height:10px;border-radius:50%;background:var(--orange)}
</style>
</head>
<body>

<div class="hero-backdrop" role="img" aria-label="Wide ocean and sky photograph behind the header"></div>

<div class="topbar"><span>USD$ ▾</span><span>English ▾</span></div>

<header class="site-header">
  <div class="brand"><span class="brand-mark"></span><span class="brand-name">Calmira Mesa</span></div>
  <nav class="main-nav">
    <a class="active" href="#">Home</a><a href="#">Destinations</a><a href="#">Our Travel</a><a href="#">Special Offers</a><a href="#">List</a><a href="#">Hotels</a><a href="#">Pages</a>
  </nav>
</header>

<section class="slider">
  <div class="slide-photo" role="img" aria-label="Tropical beach with palm trees, turquoise water and a wooden boat on the sand"></div>
  <div class="slide-copy">
    <h1>Calmira Mesa</h1>
    <p>Discover quiet beaches, guided trips and local stays across the island, planned with friendly hosts who know every cove and trail.</p>
    <span class="btn">Start Now</span>
  </div>
  <span class="slider-arrow prev"><svg width="8" height="8" viewBox="0 0 8 8"><path d="M5.5 1 2.5 4l3 3" fill="none" stroke="#555" stroke-width="1.4"/></svg></span>
  <span class="slider-arrow next"><svg width="8" height="8" viewBox="0 0 8 8"><path d="M2.5 1l3 3-3 3" fill="none" stroke="#555" stroke-width="1.4"/></svg></span>
</section>

<section class="about">
  <h2 class="section-title">About <span>us</span></h2>
  <p class="lead">Calmira Mesa brings together local tours, places to stay and ways to get around in one simple guide. Browse trusted listings, compare options and book your next trip with friendly help from the people who live here every day of the year.</p>
  <div class="services">
    <div class="service">
      <div class="service-icon"><svg width="26" height="26" viewBox="0 0 26 26"><path d="M13 3a7 7 0 0 0-7 7c0 5 7 13 7 13s7-8 7-13a7 7 0 0 0-7-7z" fill="none" stroke="#fff" stroke-width="2"/><circle cx="13" cy="10" r="2.5" fill="#fff"/></svg></div>
      <h3>Selling guided tours</h3>
      <p>Small group outings led by local guides, from river walks and coffee farms to hidden island beaches.</p>
    </div>
    <div class="service">
      <div class="service-icon"><svg width="26" height="26" viewBox="0 0 26 26"><rect x="6" y="4" width="14" height="19" fill="none" stroke="#fff" stroke-width="2"/><path d="M10 8h2M14 8h2M10 12h2M14 12h2M10 16h2M14 16h2" stroke="#fff" stroke-width="2"/><rect x="11" y="19" width="4" height="4" fill="#fff"/></svg></div>
      <h3>Hotel/Hostels</h3>
      <p>Cozy hostels and family hotels close to town, the coast and the trails, with simple online booking.</p>
    </div>
    <div class="service">
      <div class="service-icon"><svg width="28" height="26" viewBox="0 0 28 26"><path d="M4 16l3-7h14l3 7v5H4z" fill="none" stroke="#fff" stroke-width="2"/><circle cx="9" cy="21" r="2.2" fill="#fff"/><circle cx="19" cy="21" r="2.2" fill="#fff"/></svg></div>
      <h3>Rental Vehicles</h3>
      <p>Cars, scooters and bikes ready for the road, with clear daily rates and pickup right in town.</p>
    </div>
  </div>
</section>

<section class="listing">
  <h2 class="section-title">Listing Of <span>Us</span></h2>
  <div class="cards">
    <article class="card">
      <div class="card-photo beach" role="img" aria-label="Sunny beach with umbrellas along the shore"></div>
      <div class="card-body"><h4>long established fact</h4><p>A quiet stretch of sand with clear water, shaded palms and easy access from the main village road.</p>
      <div class="card-meta"><span class="stars">★★★★★</span><span>260 reviews</span></div></div>
    </article>
    <article class="card">
      <div class="card-photo hammock" role="img" aria-label="Hammock strung between palms over a sandy beach"></div>
      <div class="card-body"><h4>long established fact</h4><p>Rest in the shade by the sea, with fresh fruit stands, calm waves and sunsets over the western bay.</p>
      <div class="card-meta"><span class="stars">★★★★★</span><span>260 reviews</span></div></div>
    </article>
    <article class="card">
      <div class="card-photo city" role="img" aria-label="Coastal city skyline with a harbour at dusk"></div>
      <div class="card-body"><h4>long established fact</h4><p>Lively harbour streets with markets, cafés and evening lights, just a short ride from the island.</p>
      <div class="card-meta"><span class="stars">★★★★★</span><span>260 reviews</span></div></div>
    </article>
  </div>
</section>

<section class="contact">
  <div class="contact-box">
    <div class="contact-item"><span class="contact-icon"><svg width="12" height="12" viewBox="0 0 12 12"><path d="M6 1a3.5 3.5 0 0 0-3.5 3.5C2.5 7 6 11 6 11s3.5-4 3.5-6.5A3.5 3.5 0 0 0 6 1z" fill="#1b75bb"/></svg></span><span>ADDRESS<br>Calmira Mesa</span></div>
    <div class="contact-item"><span class="contact-icon"><svg width="12" height="12" viewBox="0 0 12 12"><path d="M3 1l2 2-1 2c1 1.5 1.5 2 3 3l2-1 2 2-1.5 2C5 11 1 7 1 2.5z" fill="#1b75bb"/></svg></span><span>1902 555 0147 / 2500 555 0182</span></div>
    <div class="contact-item"><span class="contact-icon"><svg width="12" height="12" viewBox="0 0 12 12"><rect x="1" y="3" width="10" height="7" fill="none" stroke="#1b75bb" stroke-width="1.3"/><path d="M1 3l5 4 5-4" fill="none" stroke="#1b75bb" stroke-width="1.3"/></svg></span><span>calmiramesa.example</span></div>
  </div>
</section>

<footer class="site-footer">
  <div class="footer-links"><span>HOME</span><span>ABOUT</span><span>PORTFOLIO</span><span>STORE</span><span>BLOG</span><span>CONTACT</span></div>
  <span class="copyright">Copyright © Calmira Mesa 2015</span>
  <div class="social"><span></span><span></span><span></span><span></span><span></span></div>
</footer>

</body>
</html>
```